Crowdsourced Research Platform: VELTA Polls

VELTA Polls is an acronym for Varied Estimates Linking Topical Attitudes (VELTA) Polls. This is a research effort to format and combine multiple sources of public opinion data from around the world into merged datasets. The website will at first mainly act as a quality control hub and distribution point for official dataset releases. It will provide resources such as codebooks, development guidelines, and instructional videos for crowdsourcing continued expansion of the resource. We need a coded (HTML and CSS) website design and associated files to launch the website with ease. We purchased the domain www.veltapolls.org, but access is blocked while it is under construction.

The website design should be based on a logo recently commissioned (see attached). The design should be simple and professional with lots of white space. We would like the logo on the top left of all pages and the primary navigation menu along the top-right of all pages. The primary navigation menu should have a simple mouse-over effect and the main menu items should expand with secondary drop-down options. The footer should include a few columns with headings and links to different pages. The website layout should be dynamic and expand its width to fit different sized screens. There will be a lot of data and information displayed in tables, so we would like the CSS coding and website design to include tables designed to match the website theme. The main graphical content will be data visualisations such as pie/bar charts, histograms, scatter plots, heat maps, moving average trend lines etc. We would therefore like the design to include modular sections (boxes matching theme to display plots/graphs/etc) that can visually display these types of figures with text/caption underneath to explain the data visualizations.

For more information and written placeholder content, designers should read the attached documents to get a better idea about the project. Some draft working papers using merged datsets have been included for reference and you can use these for their examples of data visualizations and use the written content for filling in page content.

Target Market(s)

The primary target audience will be academics in universities and research institutes. The resource will be most useful to quantitative social scientists, particularly political scientists and sociologists, but any discipline concerned with us humans could find the resource useful. Others such as graduate-level university students, civil servants in government departments, members of research institutions, and policy researchers in non-profit organizations will also find the resource useful.

Coding

Coded - Design and coding required

Number of Pages Required

3 page

Font styles to use
Sans Serif

Colors

Designer to choose colors to be used in the design.

Requirements
Must have
• HTML and CSS coding (not Wordpress)
Nice to have
• Content boxes to display data visualizations alongside articles.

```html
<!DOCTYPE html>
<html lang="en">
<head>
<meta charset="utf-8">
<title>VELTA Polls</title>
<link href="https://fonts.googleapis.com/css2?family=Roboto:wght@300;400;500;700;900&display=swap" rel="stylesheet">
<style>
:root{
  --brand:#1f7fc4;
  --brand-dark:#1a6fb3;
  --sky:#20a3dd;
  --sky-light:#dcedfa;
  --ink:#222;
  --text:#444;
  --muted:#777;
  --line:#e2e2e2;
  --paper:#fff;
  --grey-band:#f2f2f2;
  --tag:#dcdcdc;
  --footer:#232323;
  --footer-base:#1a1a1a;
}
*{box-sizing:border-box;margin:0;padding:0}
html,body{width:1200px;height:3333px;overflow:hidden}
body{font-family:"Roboto",Arial,sans-serif;color:var(--text);background:var(--paper);font-size:11.5px;line-height:1.55}
a{color:inherit;text-decoration:none}

/* header */
.site-header{height:69px;border-top:3px solid var(--brand);display:flex;align-items:center;justify-content:space-between;padding:0 171px 0 173px}
.brand{display:flex;align-items:center;gap:10px;color:var(--brand);font-size:27px;font-weight:500;letter-spacing:.2px}
.brand-dot{width:30px;height:30px;border-radius:50%;background:var(--brand)}
.main-nav{display:flex;gap:27px;font-size:11.5px;font-weight:500;color:#333;text-transform:uppercase}
.main-nav a:hover{color:var(--brand)}

/* hero */
.hero{position:relative;height:442px;display:flex;flex-direction:column;align-items:center;justify-content:center;color:#fff;text-align:center}
.hero-photo{position:absolute;inset:0;background:linear-gradient(160deg,#c9d6e4 0%,#8fa6bf 40%,#6f88a6 65%,#b4c3d4 100%)}
.hero-inner{position:relative;padding-top:20px}
.hero h1{font-size:44px;font-weight:700;letter-spacing:.5px;text-shadow:0 2px 6px rgba(0,0,0,.25)}
.hero p{font-size:14px;font-weight:500;text-transform:uppercase;margin-top:2px;text-shadow:0 1px 4px rgba(0,0,0,.3)}
.hero .btn-hero{display:inline-block;margin-top:36px;background:#f4f4f4;color:var(--brand);font-weight:700;font-size:14px;padding:10px 24px;border-radius:20px}

/* welcome */
.welcome{padding:45px 171px 0;text-align:center}
.welcome h2{font-size:35px;font-weight:700;color:var(--ink);letter-spacing:-.3px}
.divider{display:flex;align-items:center;justify-content:center;gap:14px;margin:14px auto 20px;width:450px}
.divider span{flex:1;height:1px;background:#bbb}
.divider i{width:22px;height:22px;border-radius:50%;border:2px solid var(--brand)}
.welcome .lead{font-size:11.5px;line-height:1.6;text-align:center;color:#444;max-width:800px;margin:0 auto}
.cards{display:flex;gap:22px;margin-top:34px}
.card{width:271px;height:300px;border:1px solid var(--line);text-align:center;padding:30px 22px 0}
.card-icon{width:84px;height:84px;border-radius:50%;background:var(--brand);margin:0 auto;display:flex;align-items:center;justify-content:center}
.card h3{color:var(--brand);font-size:18px;font-weight:700;margin:22px 0 8px;text-transform:uppercase}
.card p{font-size:11px;line-height:1.5;height:70px}
.btn-outline{display:inline-flex;align-items:center;gap:5px;border:1px solid #999;font-size:10.5px;font-weight:500;color:#333;padding:6px 14px;margin-top:14px;text-transform:uppercase}
.btn-outline.on-dark{border:2px solid #fff;color:#fff;font-weight:700;padding:8px 17px}
.btn-outline.dark{border:2px solid #333;font-weight:700;padding:8px 14px}

/* split rows */
.split{display:flex;height:347px}
.split.first{margin-top:60px}
.split .photo{width:567px;height:100%}
.split .panel{flex:1;padding:30px 40px 0;color:#fff}
.panel h2{font-size:30px;font-weight:700;margin-bottom:14px}
.panel p{font-size:11px;line-height:1.55}
.research .panel{background:var(--brand-dark);padding-left:41px}
.research .photo{background:linear-gradient(135deg,#b9c3cc 0%,#e4e7ea 40%,#8aa2c1 70%,#d8c4ad 100%)}
.release .panel{background:var(--sky);padding:26px 40px 0 173px;width:567px;flex:none}
.release .panel h2{margin-bottom:10px}
.release .panel p{font-size:10.5px;line-height:1.5}
.release .photo{flex:1;background:linear-gradient(135deg,#1c2a3a 0%,#4b5e72 45%,#8f6f4e 75%,#2d3b4d 100%)}

/* variables */
.variables{position:relative;height:612px}
.variables .photo{position:absolute;left:173px;top:112px;width:429px;height:433px;background:linear-gradient(160deg,#3a3a3a 0%,#dfe6ee 30%,#f4f6f9 60%,#c8d2de 100%)}
.variables .box{position:absolute;left:602px;top:52px;width:427px;height:426px;background:var(--sky-light);padding:24px 30px 0}
.box h2{font-size:30px;font-weight:700;color:var(--brand);margin-bottom:12px}
.box p{font-size:11px;line-height:1.55;color:#333;text-align:justify;margin-bottom:10px}

/* sources */
.sources{position:relative;height:329px;background:var(--grey-band);padding:34px 0 0 173px}
.sources h2{font-size:29px;font-weight:500;color:var(--ink);letter-spacing:-.3px}
.sources .rule{width:640px;height:1px;background:#999;margin:8px 0 12px}
.sources p{font-size:11px;width:640px;color:#333}
.tags{display:flex;flex-direction:column;gap:8px;width:640px;margin-top:16px}
.tag-row{display:flex;gap:6px}
.tag{background:var(--tag);color:#333;font-size:11px;height:28px;line-height:28px;padding:0 12px;white-space:nowrap;flex:1 1 auto}
.sources .btn-outline{margin-top:16px}
.sources .person{position:absolute;right:0;top:-18px;width:400px;height:347px;background:radial-gradient(ellipse at 50% 45%,#bdbdbd 0%,#e8e8e8 55%,rgba(242,242,242,0) 75%)}

/* contact band */
.contact{height:153px;background:var(--sky);display:flex;justify-content:center;padding-top:30px}
.contact-item{width:246px;text-align:center;color:#fff;font-size:12px;font-weight:500;text-transform:uppercase}
.contact-icon{width:58px;height:58px;border-radius:50%;background:#4bb7e6;margin:0 auto 20px;display:flex;align-items:center;justify-content:center}

/* footer */
.site-footer{height:344px;background:var(--footer);text-align:center;color:#ccc;padding-top:66px}
.subscribe{display:flex;justify-content:center}
.subscribe input{width:336px;height:37px;border:0;padding:0 12px;font-family:inherit;font-size:11px;color:#999}
.subscribe button{width:108px;height:37px;border:0;background:var(--sky);color:#fff;font-weight:700;font-size:13px;font-family:inherit}
.site-footer .brand{justify-content:center;margin-top:28px;color:var(--sky);font-size:29px}
.site-footer .brand-dot{background:var(--sky)}
.site-footer p{font-size:11px;width:800px;margin:18px auto 0;line-height:1.6}
.socials{display:flex;justify-content:center;gap:14px;margin-top:28px}
.socials span{width:38px;height:38px;border-radius:50%;border:2px solid #fff}
.copyright{height:51px;line-height:51px;background:var(--footer-base);color:#aaa;text-align:center;font-size:11px}
</style>
</head>
<body>

<header class="site-header">
  <a class="brand" href="#"><span class="brand-dot"></span>VELTA Polls</a>
  <nav class="main-nav">
    <a href="#">Home</a><a href="#">About Us</a><a href="#">Data Setup</a><a href="#">Sources</a><a href="#">Variables</a><a href="#">Contact Us</a>
  </nav>
</header>

<section class="hero">
  <div class="hero-photo" role="img" aria-label="Photo of hands reviewing printed charts and reports on a desk"></div>
  <div class="hero-inner">
    <h1>VELTA POLLS</h1>
    <p>Make it easier to work with multiple sources of public opinion data</p>
    <a class="btn-hero" href="#">SURVEYS NOW!</a>
  </div>
</section>

<section class="welcome">
  <h2>WELCOME TO VELTA POLLS</h2>
  <div class="divider"><span></span><i></i><span></span></div>
  <p class="lead">VELTA Polls make it easier to work with multiple sources of public opinion data. It does so by formatting variables for consistency and merging datasets together. The current merged dataset includes millions of respondents, covers most countries in the world, and extends back decades. This increased variation over time and space enables answering new research questions with greater reliability. The ultimate goal is to format every variable from every round of every publicly available survey source that takes nationally representative samples of adults. Furthermore, the intention is to continue this service indefinitely and independently of substantial funding, which leaves only one currently viable approach: crowdsourcing.</p>
  <div class="cards">
    <article class="card">
      <div class="card-icon"><svg width="40" height="40" viewBox="0 0 40 40" fill="#fff"><rect x="5" y="26" width="5" height="9"/><rect x="13" y="20" width="5" height="15"/><rect x="21" y="14" width="5" height="21"/><rect x="29" y="8" width="5" height="27"/><path d="M5 20 L30 5" stroke="#fff" stroke-width="2"/><path d="M26 4 L32 4 L32 10Z"/></svg></div>
      <h3>Respondent</h3>
      <p>Respondent data is composed of individuals within a country included in a survey round. Each observation is a person who responded to questions as part of a national survey.</p>
      <a class="btn-outline" href="#">Read more &#10148;</a>
    </article>
    <article class="card">
      <div class="card-icon"><svg width="40" height="40" viewBox="0 0 40 40" fill="#fff"><rect x="8" y="6" width="14" height="29"/><rect x="23" y="14" width="10" height="21"/><g fill="#1f7fc4"><rect x="11" y="10" width="3" height="3"/><rect x="16" y="10" width="3" height="3"/><rect x="11" y="16" width="3" height="3"/><rect x="16" y="16" width="3" height="3"/><rect x="11" y="22" width="3" height="3"/><rect x="16" y="22" width="3" height="3"/><rect x="26" y="18" width="4" height="3"/><rect x="26" y="24" width="4" height="3"/></g></svg></div>
      <h3>Country-Survey</h3>
      <p>Country-survey data is aggregated respondent data that preserves the structure of having different sources. Each observation represents many people within each country.</p>
      <a class="btn-outline" href="#">Read more &#10148;</a>
    </article>
    <article class="card">
      <div class="card-icon"><svg width="40" height="40" viewBox="0 0 40 40" fill="#fff"><rect x="6" y="9" width="28" height="25" rx="2"/><rect x="11" y="5" width="3" height="7"/><rect x="26" y="5" width="3" height="7"/><g fill="#1f7fc4"><rect x="10" y="17" width="4" height="4"/><rect x="18" y="17" width="4" height="4"/><rect x="26" y="17" width="4" height="4"/><rect x="10" y="25" width="4" height="4"/><rect x="18" y="25" width="4" height="4"/><rect x="26" y="25" width="4" height="4"/></g></svg></div>
      <h3>Country-Year</h3>
      <p>Country-year data pools every source for a country within a calendar year. It offers one score per nation and year for long-run comparison and trend lines.</p>
      <a class="btn-outline" href="#">Read more &#10148;</a>
    </article>
  </div>
</section>

<section class="split first research">
  <div class="photo" role="img" aria-label="Photo of a tablet showing a blue bar chart held beside paper reports"></div>
  <div class="panel">
    <h2>Crowdsourced Research</h2>
    <p>Researchers spend countless hours cleaning up datasets before working with them. Researchers repeat the same steps on the same datasets, redundantly doing work that somebody else has probably already done. Instead of working from scratch to clean up datasets, why not start with VELTA Polls, add missing variables needed for particular research projects, and then upload the additions for others to use. Using VELTA Polls as a starting point enables cost-effectively undertaking much larger projects in less time. This provides value and we will seek funding to undertake these activities, but the scale of the ambition and continuous release of new datasets necessitates crowdsourcing. The main requirement for using VELTA Polls is that you give back to the project whatever additions you make to the merged datasets and formatting scripts.</p>
    <a class="btn-outline on-dark" href="#">Read more &#10148;</a>
  </div>
</section>

<section class="split release">
  <div class="panel">
    <h2>Version 1 Release</h2>
    <p>The first version of VELTA Polls focuses on a limited set of variables: social trust, satisfaction with democracy, support for democracy, perceived electoral integrity, age, gender, education, and income. It identifies the country, year, and survey round for nineteen sources: Sahel Monitor, Hemisphere Panel, Levant Survey, Pacific Monitor, Eastern Democracy Survey, Northwind Social Survey, Civic Values Study, Unipoll: Central and Eastern, Unipoll: Standard and Special, Unipoll: Candidate Countries, Island Nations Panel, Heartland Opinion Series, Valley Voices Poll and the Southern Election Study. Future releases will expand the number of variables and sources.</p>
    <a class="btn-outline on-dark" href="#">Read more &#10148;</a>
  </div>
  <div class="photo" role="img" aria-label="Photo of a hand with a stylus over a glowing digital data display"></div>
</section>

<section class="variables">
  <div class="photo" role="img" aria-label="Photo of a laptop screen showing bar, pie and line charts"></div>
  <div class="box">
    <h2>Variables</h2>
    <p>Variables are available at three levels of analysis within each corresponding dataset: respondent, country-survey, and country-year. At the respondent level, common variables are binary and result from dichotomizing different answer scales. Neutral and midpoint answers are consistently grouped with negative answers, meaning that respondent level variables focus on measuring the presence of what it measures rather than its absence.</p>
    <p>At the country-survey level, recoded original variables are rescaled so answer values range from 0 to 100 and then averaged within each country-survey observation. This produces a single score representing the aggregated responses of all individuals surveyed within a country for a survey round. At the country-year level, the index scores represent the average of all country-survey scores. This combines overlapping country-survey scores to create unique country-year values, which are needed when merging the dataset with other country-year data. Scores range from 0 representing the lowest possible level of trust, satisfaction, or support to 100 representing the highest possible level.</p>
    <a class="btn-outline dark" href="#">Read more &#10148;</a>
  </div>
</section>

<section class="sources">
  <div class="person" role="img" aria-label="Black and white photo of a student sitting with a laptop"></div>
  <h2>Survey Sources and Years</h2>
  <div class="rule"></div>
  <p>Version 1.0 of VELTA Polls merges data from nineteen different survey sources. These are displayed below together with the range of years covered by each source.</p>
  <div class="tags">
    <div class="tag-row">
      <span class="tag">Sahel Monitor (1999-2015)</span>
      <span class="tag">Unipoll: Central and Eastern (1990-1997)</span>
      <span class="tag">Hemisphere Panel (2004-2014)</span>
    </div>
    <div class="tag-row">
      <span class="tag">Levant Survey (2006-2014)</span>
      <span class="tag">Unipoll: Standard and Special (1962-2016)</span>
      <span class="tag">Northwind Social Survey (2002-2015)</span>
    </div>
    <div class="tag-row">
      <span class="tag">Pacific Monitor (2003-2007)</span>
      <span class="tag">Civic Values Study (1981-2009)</span>
      <span class="tag">Eastern Democracy Survey (2001-2010)</span>
    </div>
  </div>
  <a class="btn-outline dark" href="#">Read more &#10148;</a>
</section>

<section class="contact">
  <div class="contact-item">
    <div class="contact-icon"><svg width="24" height="28" viewBox="0 0 24 28" fill="#fff"><path d="M12 1C6.5 1 2.5 5 2.5 10.2 2.5 17 12 27 12 27S21.5 17 21.5 10.2C21.5 5 17.5 1 12 1Z"/><circle cx="12" cy="10" r="3.6" fill="#4bb7e6"/></svg></div>
    New York 4120 Elm Avenue
  </div>
  <div class="contact-item">
    <div class="contact-icon"><svg width="26" height="20" viewBox="0 0 26 20"><rect x="1" y="1" width="24" height="18" rx="2" fill="#fff"/><path d="M2 3 L13 11 L24 3" stroke="#4bb7e6" stroke-width="2" fill="none"/></svg></div>
    contact@veltapolls.org
  </div>
  <div class="contact-item">
    <div class="contact-icon"><svg width="24" height="24" viewBox="0 0 24 24" fill="#fff"><path d="M6 1 L9.5 6.5 7.5 9C9 12 12 15 15 16.5L17.5 14.5 23 18 20.5 22C12 23 1 12 2 3.5Z"/></svg></div>
    Telephone: +1 800 555 0142
  </div>
  <div class="contact-item">
    <div class="contact-icon"><svg width="26" height="24" viewBox="0 0 26 24" fill="#fff"><rect x="7" y="1" width="12" height="7"/><rect x="1" y="8" width="24" height="10" rx="2"/><rect x="7" y="14" width="12" height="9" stroke="#4bb7e6" stroke-width="1.5"/></svg></div>
    Fax: +1 800 555 0178
  </div>
</section>

<footer class="site-footer">
  <form class="subscribe"><input type="email" placeholder="Enter Your Email id"><button type="button">SUBSCRIBE</button></form>
  <a class="brand" href="#"><span class="brand-dot"></span>VELTA Polls</a>
  <p>Merged public opinion datasets built and shared by a community of researchers. Join the list to hear about new releases, codebooks and guidelines. Every addition you upload helps others start their work from cleaner data and finish sooner.</p>
  <div class="socials"><span aria-label="Social link"></span><span aria-label="Social link"></span><span aria-label="Social link"></span></div>
</footer>
<div class="copyright">© 2018 veltapolls.org. All rights reserved.</div>

</body>
</html>
```